Envelope Design Project

I will need two envelopes to be designed:-

DL size
C4 size

Please see uploaded documents for Design specs:

1) Design specs provided by printer (doc called DL Envelope Specs)
2) Design specs to comply with Kestrel Mailways requirements (doc called Kestrel Mailways Envelope Design Requirements)

Please adhere to the above for final design. Many thanks.

Target Market(s)

Real Estate Agents, Strata Managers, Builders, Architects, Business Owners

Industry/Entity Type

Printer

Requirements
Must have
• In top left corner
- Logo
- Return address - Unit 8, 19 Wattlebark Rd, Brindle, VIC 3915

```html
<!DOCTYPE html>
<html lang="en">
<head>
<meta charset="utf-8">
<title>Tarrin Asbestos &amp; Safety – Envelope Set</title>
<link rel="stylesheet" href="https://fonts.googleapis.com/css2?family=Jost:wght@500&display=swap">
<style>
  :root {
    --backdrop: #ececec;
    --paper: #f5f5f5;
    --band-top: #29233f;
    --band-bottom: #3d3372;
    --brand-ink: #262140;
    --brand-accent: #9dc33b;
    --address-ink: #6b6b6b;
  }
  html, body {
    margin: 0;
    padding: 0;
    width: 1200px;
    height: 1000px;
    overflow: hidden;
    background: var(--backdrop);
    font-family: "Jost", Arial, sans-serif;
  }
  .canvas {
    position: relative;
    width: 1200px;
    height: 1000px;
  }
  .envelope {
    position: absolute;
    background: var(--paper);
    overflow: hidden;
  }
  .envelope--dl { left: 85px; top: 67px; width: 530px; height: 264px; }
  .envelope--c4 { left: 345px; top: 404px; width: 757px; height: 536px; }

  .side-band {
    position: absolute;
    left: 0;
    top: 0;
    bottom: 0;
    background: linear-gradient(180deg, var(--band-top), var(--band-bottom));
  }
  .envelope--dl .side-band { width: 44px; }
  .envelope--c4 .side-band { width: 59px; }

  .logo-tab {
    position: absolute;
    background: var(--paper);
  }
  .envelope--dl .logo-tab { left: 16px; top: 36px; width: 60px; height: 72px; border-radius: 9px; }
  .envelope--c4 .logo-tab { left: 23px; top: 48px; width: 80px; height: 104px; border-radius: 14px; }

  .brand {
    position: absolute;
    display: flex;
    align-items: flex-start;
    color: var(--brand-ink);
    font-weight: 500;
  }
  .brand__mark { background: var(--brand-accent); flex: none; }
  .brand__name { line-height: 1; }
  .brand__line { display: block; }
  .brand__line--main { letter-spacing: 0.5px; }
  .brand__line--sub { letter-spacing: 0.3px; }

  .envelope--dl .brand { left: 30px; top: 48px; gap: 7px; }
  .envelope--dl .brand__mark { width: 24px; height: 24px; margin-top: 3px; border-radius: 4px; }
  .envelope--dl .brand__line--main { font-size: 28px; }
  .envelope--dl .brand__line--sub { font-size: 10px; margin-top: 4px; }

  .envelope--c4 .brand { left: 40px; top: 66px; gap: 10px; }
  .envelope--c4 .brand__mark { width: 38px; height: 38px; margin-top: 4px; border-radius: 6px; }
  .envelope--c4 .brand__line--main { font-size: 44px; }
  .envelope--c4 .brand__line--sub { font-size: 15.5px; margin-top: 6px; }

  .return-address {
    position: absolute;
    margin: 0;
    color: var(--address-ink);
    font-style: normal;
    font-family: Arial, Helvetica, sans-serif;
  }
  .envelope--dl .return-address { left: 64px; top: 210px; font-size: 7.5px; line-height: 10px; }
  .envelope--c4 .return-address { left: 88px; top: 451px; font-size: 11px; line-height: 15px; }
</style>
</head>
<body>
<main class="canvas">
  <section class="envelope envelope--dl" aria-label="DL envelope">
    <div class="side-band"></div>
    <div class="logo-tab"></div>
    <div class="brand">
      <span class="brand__mark"></span>
      <span class="brand__name">
        <span class="brand__line brand__line--main">Tarrin</span>
        <span class="brand__line brand__line--sub">ASBESTOS &amp; SAFETY</span>
      </span>
    </div>
    <address class="return-address">Unit 8, 19 Wattlebark Rd<br>Brindle, VIC 3915</address>
  </section>

  <section class="envelope envelope--c4" aria-label="C4 envelope">
    <div class="side-band"></div>
    <div class="logo-tab"></div>
    <div class="brand">
      <span class="brand__mark"></span>
      <span class="brand__name">
        <span class="brand__line brand__line--main">Tarrin</span>
        <span class="brand__line brand__line--sub">ASBESTOS &amp; SAFETY</span>
      </span>
    </div>
    <address class="return-address">Unit 8, 19 Wattlebark Rd<br>Brindle, VIC 3915</address>
  </section>
</main>
</body>
</html>
```